The Open Compass Field Journeys Travel Brochure

I'm looking for a brochure design for a new travel product - The Open Compass Field Journeys, catering for students above 12 years old. Target audience are schools that do destination projects. Brochure to be read by head teacher, parents and students.

Brochure should be A4 in size, 4-6 pages. Format of brochure is hard cover (a folder) with inlet for flyers. Flyers for destinations will be updated from time to time.

Finished job needs to be converted to electronic format for website and email proposal usage.

Attached is text to be used on brochure. Order of section can be adjusted.

For "Elements of the trip", please understand the contents and explain/display it in a graphic form.

For flyer, please come out with a template that I can use for other destinations. The main elements - what's included, number of days, location for pictures, itinerary, educational focus, should be alterable. Attached are text for two sample destinations.
Also attached (tour itinerary example) a version of flyer that I like.

I'm attaching some pictures here. If you find more suitable pictures, please feel free to use them.

Reason: I'm extending the deadline of this project by 4 days, as I need to add details & photo of another travel specialist in personnel session (total of 3 members). Also, in view of the amount of work a designer has to do for this project, I'm giving you more time for submission. Please do not hesitate to be in touch should you need more than 4 days extension. Thank you.

Target Market(s)

Schools - especially the head teacher and parents, to send students above 12 years old to travel

Industry/Entity Type

Electronic

Requirements
Must have
• This is a travel brochure with education elements in it. Parents feel better when their children are travelling for a purpose and lead by responsible teachers/adults whom they can trust. So, the design has to emphasis that education elements and safety are our utmost priority.
Nice to have
• We specialise in environmental study. So, it is nice to have the environmental touch in the design.
Should not have
• Our target market segment is the Middle East, which can be quite sensitive to religion. I prefer not to have any religious related illustration on the design.

```html
<!DOCTYPE html>
<html lang="en">
<head>
<meta charset="utf-8">
<title>The Open Compass Field Journeys – Elements of the Trips</title>
<link href="https://fonts.googleapis.com/css2?family=Patua+One&family=Source+Sans+3:wght@400;700&display=swap" rel="stylesheet">
<style>
  :root {
    --green: #3aa935;
    --green-dark: #2e8f2b;
    --green-light: #8dc63f;
    --green-inner: #7cc142;
    --ink: #1a1a1a;
    --paper: #ffffff;
  }
  * { margin: 0; padding: 0; box-sizing: border-box; }
  html, body { width: 864px; height: 1200px; overflow: hidden; background: var(--paper); }
  .page {
    position: relative;
    width: 800px; height: 1111px;
    transform: scale(1.08); transform-origin: 0 0;
    font-family: "Source Sans 3", "Myriad Pro", Arial, sans-serif;
    color: var(--ink);
  }
  .page-title {
    position: absolute; left: 62px; top: 96px;
    font-family: "Patua One", Georgia, serif;
    font-size: 22px; color: var(--green); font-weight: 400;
  }
  .wheel { position: absolute; left: 0; top: 0; }
  .element { position: absolute; font-size: 10px; line-height: 12px; }
  .element h3 {
    font-family: "Patua One", Georgia, serif;
    font-weight: 400; color: var(--green);
    font-size: 16.5px; line-height: 16.5px; margin-bottom: 2px;
  }
  .hub-label {
    position: absolute; left: 300px; top: 470px; width: 200px;
    text-align: center; color: #fff;
    font-family: "Patua One", Georgia, serif;
    font-size: 29px; line-height: 37px; letter-spacing: 0.5px;
  }
  .closing-note {
    position: absolute; left: 62px; top: 962px; width: 332px;
    font-size: 16px; line-height: 20px; text-align: justify;
  }
  .closing-note .lead { font-weight: 700; font-variant: small-caps; font-size: 17px; }
</style>
</head>
<body>
<div class="page">
  <h2 class="page-title">What are the elements of the trips?</h2>

  <svg class="wheel" width="800" height="1111" viewBox="0 0 800 1111">
    <g class="spokes-outer" stroke="var(--green-light)" stroke-width="1.2">
      <line x1="316" y1="192" x2="322" y2="300"/>
      <line x1="523" y1="216" x2="485" y2="305"/>
      <line x1="92" y1="376" x2="195" y2="440"/>
      <line x1="712" y1="377" x2="645" y2="430"/>
      <line x1="47" y1="614" x2="155" y2="595"/>
      <line x1="757" y1="598" x2="650" y2="585"/>
      <line x1="200" y1="830" x2="260" y2="750"/>
      <line x1="640" y1="822" x2="560" y2="745"/>
      <line x1="400" y1="912" x2="400" y2="795"/>
    </g>
    <g class="dots-outer" fill="var(--green-light)">
      <circle cx="316" cy="192" r="4.5"/><circle cx="523" cy="216" r="4.5"/>
      <circle cx="92" cy="376" r="4.5"/><circle cx="712" cy="377" r="4.5"/>
      <circle cx="47" cy="614" r="4.5"/><circle cx="757" cy="598" r="4.5"/>
      <circle cx="200" cy="830" r="4.5"/><circle cx="640" cy="822" r="4.5"/>
      <circle cx="400" cy="912" r="4.5"/>
    </g>
    <g class="spokes-main" stroke="var(--green)" stroke-width="2.5">
      <line x1="400" y1="545" x2="400" y2="290"/>
      <line x1="400" y1="545" x2="575" y2="352"/>
      <line x1="400" y1="545" x2="225" y2="352"/>
      <line x1="400" y1="545" x2="138" y2="515"/>
      <line x1="400" y1="545" x2="670" y2="515"/>
      <line x1="400" y1="545" x2="635" y2="690"/>
      <line x1="400" y1="545" x2="180" y2="690"/>
      <line x1="400" y1="545" x2="305" y2="815"/>
      <line x1="400" y1="545" x2="487" y2="815"/>
    </g>
    <circle class="ring" cx="400" cy="545" r="255" fill="var(--green)"/>
    <g class="dots-main" fill="var(--green)">
      <circle cx="400" cy="290" r="10"/><circle cx="575" cy="352" r="10"/>
      <circle cx="225" cy="352" r="10"/><circle cx="138" cy="515" r="10"/>
      <circle cx="670" cy="515" r="10"/><circle cx="635" cy="690" r="10"/>
      <circle cx="180" cy="690" r="10"/><circle cx="305" cy="815" r="10"/>
      <circle cx="487" cy="815" r="10"/>
    </g>
    <circle class="hub" cx="400" cy="545" r="114" fill="var(--green-inner)" stroke="#6ab33a" stroke-width="3"/>

    <g class="icons">
      <rect role="img" aria-label="Itinerary notebook icon" x="372" y="350" width="58" height="78" rx="6" fill="var(--green-light)"/>
      <rect role="img" aria-label="Full time tour director icon" x="465" y="395" width="75" height="68" rx="6" fill="var(--green-dark)"/>
      <rect role="img" aria-label="Bed icon for accommodation" x="248" y="398" width="82" height="58" rx="6" fill="var(--green-dark)"/>
      <rect role="img" aria-label="Visa card icon" x="526" y="505" width="80" height="40" rx="4" fill="var(--green-light)"/>
      <rect role="img" aria-label="Air ticket icon" x="192" y="512" width="92" height="36" rx="4" fill="var(--ink)"/>
      <rect role="img" aria-label="Local tour guide icon" x="510" y="585" width="62" height="85" rx="6" fill="var(--green-light)"/>
      <rect role="img" aria-label="Travel insurance shield icon" x="222" y="600" width="68" height="80" rx="10" fill="var(--green-light)"/>
      <rect role="img" aria-label="Food and drinks icon" x="305" y="660" width="88" height="80" rx="8" fill="var(--green-dark)"/>
      <rect role="img" aria-label="Hands icon for local collaboration" x="412" y="645" width="88" height="95" rx="8" fill="var(--green-dark)"/>
    </g>
  </svg>

  <div class="hub-label">WHAT'S<br>INCLUDED<br>IN THE<br>COST?</div>

  <section class="element" style="left:327px; top:162px; width:158px;">
    <h3>Tours</h3>
    <p>We will design an itinerary for the students to explore the essence of each destination. During the visits, we will incorporate educational element, be it environmental, geographical, historical or cultural. We will ensure stimulating experiences throughout the journey with suitable time for reflection and relaxation.</p>
  </section>

  <section class="element" style="left:590px; top:212px; width:150px;">
    <h3>Full time<br>tour director</h3>
    <p>This person is your guide, friend and support throughout the tour. We will have at least one director on the trip, to travel with the group from the UAE and throughout the journey. Ratio is 1:8, 1 tour director or teacher to eight students.</p>
  </section>

  <section class="element" style="left:118px; top:272px; width:180px;">
    <h3>Accommodation</h3>
    <p>We organise suitable lodging for students at strategic location with best quality, where they can interact with their friends and meet local residents.</p>
  </section>

  <section class="element" style="left:683px; top:468px; width:62px;">
    <h3>Visa</h3>
    <p>We will assist with entry visas for all of the participants.</p>
  </section>

  <section class="element" style="left:63px; top:481px; width:60px;">
    <h3>Air<br>ticket</h3>
    <p>We will arrange the best flight options available to you.</p>
  </section>

  <section class="element" style="left:638px; top:707px; width:124px;">
    <h3>Local tour<br>guide</h3>
    <p>We will have licensed local guides with extensive knowledge about each destination for specific location.</p>
  </section>

  <section class="element" style="left:75px; top:690px; width:128px;">
    <h3>Travel<br>insurance</h3>
    <p>Travel insurance for each of the students is compulsory and can be arranged by Open Compass Learning.</p>
  </section>

  <section class="element" style="left:232px; top:833px; width:155px;">
    <h3>Food &amp; drinks</h3>
    <p>We will include all meals throughout the journey, ensuring quality and suitability at each of the destinations.</p>
  </section>

  <section class="element" style="left:488px; top:833px; width:134px;">
    <h3>Local<br>collaboration</h3>
    <p>We can arrange collaboration with local community, based on your requirements. For instance, school visit, charity fundraising, orphanage support, etc.</p>
  </section>

  <p class="closing-note"><span class="lead">Any situations that arise on the trips,</span> be it minor or major issues, will be handled professionally and promptly by our tour directors.</p>
</div>
</body>
</html>
```